business card design for luxurious real estate brand

using the attached logo, i am looking for a 2-sided business card design. the back should be the gold logo on black background. the front needs to include: gold logo, name, phone, email, and website

Industry/Entity Type

real estate

Contact Information for Business Card

logo, name, email, phone, website

Font styles to use
Sans Serif

```html
<!DOCTYPE html>
<html lang="en">
<head>
<meta charset="utf-8">
<title>Casa Lumera – Business Card</title>
<link href="https://fonts.googleapis.com/css2?family=Open+Sans:wght@400;600;700&display=swap" rel="stylesheet">
<style>
  :root {
    --backdrop: #161616;
    --card: #2a2828;
    --card-edge: #333131;
    --gold: #f7c81e;
    --ink-light: #f2f2f2;
  }
  * { box-sizing: border-box; margin: 0; padding: 0; }
  html, body {
    width: 1200px; height: 900px; overflow: hidden;
    background: var(--backdrop);
    font-family: "Open Sans", Arial, sans-serif;
  }
  .sheet {
    width: 1200px; height: 900px;
    display: flex; flex-direction: column; align-items: center; justify-content: center;
    gap: 36px;
  }
  .card {
    position: relative;
    width: 680px; height: 388px;
    background: var(--card);
    border: 1px solid var(--card-edge);
    box-shadow: 0 12px 30px rgba(0,0,0,.55);
  }
  .brand {
    display: flex; align-items: center; gap: 14px;
    color: var(--gold);
    font-weight: 600;
    letter-spacing: .28em;
    text-transform: uppercase;
    white-space: nowrap;
  }
  .brand-square { width: 14px; height: 14px; background: var(--gold); flex: none; }

  /* back side */
  .card--back { display: flex; align-items: center; justify-content: center; }
  .card--back .brand { font-size: 34px; }
  .card--back .brand-square { width: 22px; height: 22px; }

  /* front side */
  .card--front .brand { position: absolute; left: 56px; top: 78px; font-size: 22px; }
  .divider {
    position: absolute; left: 40px; top: 176px;
    width: 460px; height: 2px; background: var(--gold);
  }
  .contact-list {
    position: absolute; left: 40px; top: 236px;
    list-style: none; color: var(--ink-light); font-size: 17px; line-height: 1.5;
  }
  .contact-list li { display: flex; align-items: center; gap: 8px; }
  .contact-icon { width: 16px; height: 16px; flex: none; }
  .holder {
    position: absolute; right: 52px; top: 214px; text-align: right;
  }
  .holder-name { color: var(--gold); font-weight: 700; font-size: 22px; letter-spacing: .01em; }
  .holder-role { color: var(--ink-light); font-size: 17px; margin-top: 2px; }
  .accent-bar {
    position: absolute; right: 20px; top: 226px;
    width: 10px; height: 52px; background: var(--gold);
  }
</style>
</head>
<body>
<main class="sheet">
  <section class="card card--back" aria-label="Card back">
    <div class="brand"><span class="brand-square"></span>Casa Lumera</div>
  </section>

  <section class="card card--front" aria-label="Card front">
    <div class="brand"><span class="brand-square"></span>Casa Lumera</div>
    <div class="divider"></div>
    <ul class="contact-list">
      <li>
        <svg class="contact-icon" viewBox="0 0 16 16" aria-hidden="true"><path fill="#f7c81e" d="M3.5 1.5l2.5 3-1.5 1.5c.8 1.8 2.2 3.2 4 4l1.5-1.5 3 2.5-1.5 2.5C6.5 13.5 2.5 9.5 1 3z"/></svg>
        (777) 777-7777
      </li>
      <li>
        <svg class="contact-icon" viewBox="0 0 16 16" aria-hidden="true"><rect x="1" y="3" width="14" height="10" fill="#f7c81e"/><path d="M1 3l7 6 7-6" fill="none" stroke="#2a2828" stroke-width="1.4"/></svg>
        yourmailinfo@email
      </li>
      <li>
        <svg class="contact-icon" viewBox="0 0 16 16" aria-hidden="true"><circle cx="8" cy="8" r="7" fill="#f7c81e"/><path d="M1 8h14M8 1c-3 3.5-3 10.5 0 14M8 1c3 3.5 3 10.5 0 14" fill="none" stroke="#2a2828" stroke-width="1.1"/></svg>
        www.yourwebsite.com
      </li>
    </ul>
    <div class="holder">
      <div class="holder-name">MARCUS HALE</div>
      <div class="holder-role">Founder</div>
    </div>
    <div class="accent-bar"></div>
  </section>
</main>
</body>
</html>
```